business card for an electronic retail store

take our existing color logo, design a new business card and make a black&white version of the logo as well

Industry/Entity Type

Electronic

```html
<!DOCTYPE html>
<html lang="en">
<head>
<meta charset="utf-8">
<title>Streetline Business Card</title>
<link rel="stylesheet" href="https://fonts.googleapis.com/css2?family=Tinos&family=Cinzel:wght@500&family=Josefin+Sans:wght@400&display=swap">
<style>
  :root {
    --backdrop: #d9d7d3;
    --card-black: #0c0c0c;
    --brand-red: #d81f26;
    --brand-red-deep: #a8141a;
    --ink-white: #f2f2f2;
    --ink-dark: #1a1a1a;
  }
  * { margin: 0; padding: 0; box-sizing: border-box; }
  html, body { width: 1200px; height: 871px; overflow: hidden; }
  body { background: var(--backdrop); position: relative; }

  .card {
    position: absolute;
    width: 560px;
    height: 320px;
    background: var(--card-black);
    box-shadow: 0 10px 28px rgba(0,0,0,0.35);
    overflow: hidden;
  }
  .card--front { left: 80px; top: 70px; display: flex; align-items: center; justify-content: center; }
  .card--back { left: 560px; top: 480px; display: flex; }

  .brand {
    display: flex;
    flex-direction: column;
    align-items: flex-start;
  }
  .brand__name {
    font-family: "Tinos", serif;
    font-weight: 400;
    color: var(--ink-white);
    letter-spacing: 3px;
    line-height: 1;
    white-space: nowrap;
  }
  .brand__tagline {
    font-family: "Tinos", serif;
    color: var(--ink-white);
    margin-top: 10px;
    white-space: nowrap;
  }

  .card--front .brand__name { font-size: 46px; }
  .card--front .brand__tagline { font-size: 21px; }

  .back__brand-side {
    width: 46%;
    display: flex;
    align-items: center;
    justify-content: center;
  }
  .back__brand-side .brand__name { font-size: 28px; letter-spacing: 2px; }
  .back__brand-side .brand__tagline { font-size: 14px; margin-top: 8px; }

  .back__contact-side {
    width: 54%;
    background: linear-gradient(160deg, var(--brand-red) 0%, var(--brand-red-deep) 100%);
    padding: 46px 34px;
    color: var(--ink-dark);
  }
  .contact__name {
    font-family: "Cinzel", serif;
    font-weight: 500;
    font-size: 17px;
    letter-spacing: 1.5px;
  }
  .contact__role {
    font-family: "Josefin Sans", sans-serif;
    font-size: 13px;
    margin-top: 4px;
  }
  .contact__address {
    font-family: "Josefin Sans", sans-serif;
    font-size: 13px;
    line-height: 1.45;
    margin-top: 34px;
  }
  .contact__list { list-style: none; margin-top: 14px; }
  .contact__item {
    display: flex;
    align-items: center;
    gap: 12px;
    font-family: "Josefin Sans", sans-serif;
    font-size: 13px;
    line-height: 1.75;
  }
  .contact__icon { width: 14px; height: 14px; flex: none; }
  .contact__icon path, .contact__icon rect { fill: none; stroke: var(--ink-white); stroke-width: 1.3; }
</style>
</head>
<body>

<section class="card card--front" aria-label="Card front">
  <div class="brand">
    <span class="brand__name">STREETLINE</span>
    <p class="brand__tagline">Car Audio • Performance • Security</p>
  </div>
</section>

<section class="card card--back" aria-label="Card back">
  <div class="back__brand-side">
    <div class="brand">
      <span class="brand__name">STREETLINE</span>
      <p class="brand__tagline">Car Audio • Performance • Security</p>
    </div>
  </div>
  <div class="back__contact-side">
    <p class="contact__name">Daniel Morvan</p>
    <p class="contact__role">President</p>
    <p class="contact__address">2480 Harbor Crest Way<br>Oceanside, CA 92054</p>
    <ul class="contact__list">
      <li class="contact__item">
        <svg class="contact__icon" viewBox="0 0 14 14"><path d="M2 5 Q7 1 12 5 L10 7 L8.5 5.5 L5.5 5.5 L4 7 Z M3 8 H11 V12 H3 Z"/></svg>
        555-014-2281
      </li>
      <li class="contact__item">
        <svg class="contact__icon" viewBox="0 0 14 14"><rect x="4" y="1" width="6" height="12" rx="1"/></svg>
        555-019-7064
      </li>
      <li class="contact__item">
        <svg class="contact__icon" viewBox="0 0 14 14"><rect x="1" y="3" width="12" height="8"/><path d="M1 3 L7 8 L13 3"/></svg>
        info@streetline.com
      </li>
    </ul>
  </div>
</section>

</body>
</html>
```